Implant and Mini Implant trifold brochure.

Logo is attached. Our website: www.q7rdental.com

We need an Implant and Mini Implant Flyer (on the same flyer) to be done by someone experienced in Dental marketing.

To be mailed via : Each Block Bulk Post-Counter® (EBBP Counter®)
You need to put a Retail Indica
Reference: https://www.natpostal.example/business/each-block-bulk-post.htm
Each Block Bulk Post-Counter Indicia Guidelines

Every EBBP mailpiece must have an EBBP indicia with “ECRWSS” in the address area, within the permit indicia, or below the permit, like the examples to the right.
The EBBP Counter Indicia does not have a specific size requirement but must be larger than .5" x .5".
The type font must be in all caps and at least a 4 point size.
Place the indicia in the upper right hand corner of the mailpiece.
It should fit in the area 1.625" from the right edge and 1.375" from top edge.
Leave 1/8" of space around the top and right edge.

There should be a picture of a senior citizen eating apple - that is what implants will provide.

One side English; Other side Spanish.

If you do not have idea on what implants and mini-implants are then please ask specific questions.

Make space for specials.

Target Market(s)

dental implants, dental mini implants

Font styles to use
Other font styles liked:
• leaving it open for designer.

Colors
00a990
33b8a4
87cfc6
cadf82

Requirements
Must have
• A senior citizen eating apple - that is what implants allow people to do.
• Once the design layout is finalized, we will provide text. I am leaving the design wide open. you may look at good templates for ideas, but please respect the copyright.
Nice to have
• Use implant and mini implant pictures.
• Images needed
• 1) 3 Easy Steps to Implant Restoration in 1 visit: Use three images: mouth with missing teeth; mouth with implant screws fitted; mouth with teeth restored.
• 2) Image for Implant based Denture.
• 3) Senior Citizen or a couple eating apple.
• Image must be of good quality; even if taken from different sources they must gel well with the over all design. The final design has to be stunning.
• Please do not provide me with designs that I can get from any printing company.
• The Text area:
• 1. Why Implants?
• 2. Space for implant based dentures.
• 3. Other spaces for filling in "Why visit q7r Dental"
• Additional Info: Time to use the following text in the final output.
• q7r Dental - Your base for Crown-to-Root Dental care.
• q7r Dental - Your Implant Harbor.
• Why Implants?
• . Durable, long lasting teeth replacement
• . Surgically implanted metal posts or frames into the jawbone
• . Allows crowns, bridges or complete dentures to be placed on implants
• Why Implant Dentures?
• . Durable and Cost Effective
• . Your denture fabricated as normal denture
• . Four or more implants are placed in one visit
• . Your denture is then retrofitted to snap on the mini implant retention head
• . Stabilize your loose dentures in one visit
• Why Mini Implants?
• . Less involved procedure than conventional implants
• . Usually completed in one dental appointment
• . Replace missing teeth instantly
• Implants vs Mini-Implants
• Visit q7r Dental for a complementary consultation to learn which option is best for you. Depending on various conditions including that of the jawbone, you may be recommended an implant or mini-implant based treatment.
• Implant or Mini-implant treatment may not be suitable for all patients. For implants to be successful, you need to have healthy gums and adequate bones to support the implants. You must also be willing to commit to proper maintenance of your implants or dentures. Visit your dentist at q7r Dental to learn more.
• Spanish translation from google added below:
• q7r Dental: su base para atención Corona-a-Raíz dental.
• q7r Dental: su puerto de implante.
• ¿Por qué los implantes?
• . Reemplazo duradero y duradero de los dientes
• . Puestos o marcos de metal implantados quirúrgicamente en la mandíbula
• . Permiten para colocan coronas, puentes o dentaduras completas en implantes
• ¿Por qué las dentaduras postizas?
• . Durable y rentable
• . Su dentadura fabricada como dentadura normal
• . Cuatro o más implantes se colocan en una visita
• . Su dentadura se reajusta para encajar en el cabezal de retención mini implante
• . Estabilice sus dentaduras sueltas en una visita
• ¿Por qué Mini Implantes?
• . Procedimiento menos complicado que los implantes convencionales
• . Generalmente se completa en una cita dental
• . Reemplace los dientes perdidos al
• Implantes vs Mini Implantes
• Visite q7r Dental para obtener una consulta complementaria y conocer cuál es la mejor opción para usted. Dependiendo de varias condiciones, incluida de la mandíbula, se le puede recomenda un tratamiento basado en implantes o mini-implantes.
• El tratamiento con implantes o mini-implantes puede no ser adecuado para todos los pacientes. Para que los implantes tengan éxito, debe tener encías sanas y huesos adecuados para apoyar los implantes. También debe estar dispuesto a comprometerse con el mantenimiento adecuado de sus implantes o dentaduras postizas. Visite a su dentista en q7r Dental para obtener más información.
Should not have
• blank spaces without purpose

```html
<!DOCTYPE html>
<html lang="en">
<head>
<meta charset="utf-8">
<title>q7r Dental – Trifold Brochure</title>
<link href="https://fonts.googleapis.com/css2?family=Open+Sans:wght@400;600;700;800&display=swap" rel="stylesheet">
<style>
:root{
  --teal:#00a990;
  --teal-mid:#33b8a4;
  --teal-soft:#87cfc6;
  --teal-pale:#dff3ef;
  --lime:#cadf82;
  --blue:#1f6fb5;
  --navy:#1d3a4f;
  --ink:#3c4a52;
  --page:#ffffff;
  --stage:#e9ecec;
}
*{box-sizing:border-box;margin:0;padding:0}
html,body{width:893px;height:1200px;overflow:hidden}
body{background:var(--stage);font-family:"Open Sans",sans-serif;color:var(--ink);position:relative}
.sheet{position:absolute;left:30px;width:833px;height:560px;background:var(--page);overflow:hidden;box-shadow:0 2px 10px rgba(0,0,0,.18)}
.sheet--outside{top:30px}
.sheet--inside{top:610px}
.panel{position:absolute;top:0;width:277.67px;height:560px}
.panel--1{left:0}.panel--2{left:277.67px}.panel--3{left:555.33px}
.fold{position:absolute;top:0;width:1px;height:560px;background:rgba(0,0,0,.06)}
.photo{position:absolute}
.photo--circle{border-radius:50%;border:6px solid var(--teal);box-shadow:0 0 0 3px #fff}
.body-text{position:absolute;font-size:7.2px;line-height:1.5;color:var(--ink)}
.body-text p+p{margin-top:6px}
.body-text strong{color:var(--navy)}
.tab{position:absolute;background:var(--teal);color:#fff;font-weight:700;font-size:9.5px;padding:3px 12px;border-radius:0 10px 10px 0}
.brand-name{position:absolute;font-weight:700;font-size:19px;color:var(--navy);letter-spacing:.2px;white-space:nowrap}
.contact{position:absolute;font-size:9px;color:var(--navy)}
.contact li{list-style:none;display:flex;align-items:flex-start;gap:8px;margin-bottom:9px}
.contact svg{flex:none;margin-top:1px}
.indicia{position:absolute;border:1px solid var(--navy);background:#fff;font-size:5px;line-height:1.35;text-align:center;padding:3px;font-weight:700;color:var(--navy)}
.address-block{position:absolute;transform:rotate(90deg);transform-origin:left top;font-size:7px;line-height:1.5;color:var(--navy);background:#fff;border:1px solid #b8c4c8;padding:4px 8px;width:120px}
.tagline{position:absolute;left:0;width:277px;text-align:center;color:var(--navy)}
.tagline__lead{font-size:15px;font-weight:700}
.tagline__big{font-size:30px;font-weight:800;color:var(--blue);line-height:1}
.tagline__tail{font-size:14px;font-weight:700}
</style>
</head>
<body>

<section class="sheet sheet--outside" aria-label="Brochure outside">
  <svg class="photo" style="left:0;top:0" width="833" height="560" aria-hidden="true">
    <path d="M0 250 Q140 215 277.67 250 L277.67 560 L0 560 Z" fill="var(--teal-pale)"/>
    <path d="M0 480 Q140 505 277.67 480 L277.67 560 L0 560 Z" fill="var(--teal-soft)"/>
    <rect x="277.67" y="0" width="277.67" height="300" fill="var(--teal-pale)"/>
    <path d="M277.67 250 Q416 330 555.33 250 L555.33 300 L277.67 300 Z" fill="#fff"/>
    <path d="M555.33 300 Q690 250 833 300 L833 560 L555.33 560 Z" fill="var(--teal-pale)"/>
    <path d="M555.33 320 Q690 270 833 320" stroke="var(--teal-soft)" stroke-width="10" fill="none"/>
    <path d="M590 78 Q700 50 833 70" stroke="var(--lime)" stroke-width="5" fill="none"/>
  </svg>

  <div class="panel panel--1">
    <div class="photo" style="left:0;top:0;width:277.67px;height:205px;background:linear-gradient(135deg,#e8ece9,#c9d8cf 55%,#a9c4b2)" role="img" aria-label="Photo of a dentist smiling beside a patient in the dental chair"></div>
    <div class="photo photo--circle" style="left:70px;top:150px;width:130px;height:130px;background:radial-gradient(circle,#9cc8e8,#5a94c6 70%)" role="img" aria-label="Photo of gloved hands showing a dental jaw model"></div>
    <div class="body-text" style="left:20px;top:300px;width:240px">
      <p><strong>"q7r Dental"</strong> is "Crown-to-Root Dental" - Your home for Crown-to-Root dental care in Greenfield and Oakbrook, in the region. We accept most insurance plans. The friendly staff at q7r Dental aims to provide individuals with a comfortable and relaxing environment where we strive to meet and exceed your expectations through professional results.</p>
    </div>
    <div class="tab" style="left:0;top:392px">We are a Practice</div>
    <div class="body-text" style="left:20px;top:416px;width:240px">
      <p>We believe that general dentistry is not an art, but is the practicing of pursuing one's discipline with discipline year after year, to hone the skills that ultimately helps a practitioner produce results of highest quality, in a repeatable fashion. Yes, that is what we aim for - to acquire the skill of providing quality care for your crowns-to-roots. Dentistry is, therefore, also a practice of learning with each smile we hope to bring.</p>
    </div>
  </div>
  <div class="fold" style="left:277.67px"></div>

  <div class="panel panel--2">
    <div class="indicia" style="left:224px;top:10px;width:44px;height:46px">PRSRT STD<br>US POSTAGE<br>PAID<br>EBBP COUNTER</div>
    <div class="address-block" style="left:190px;top:10px">*********ECRWSS*******<br>Postal Customer<br>City, State ZIP Code</div>
    <div class="photo photo--circle" style="left:60px;top:140px;width:150px;height:150px;background:radial-gradient(circle at 50% 40%,#f5e3d6,#dcb9a0 60%,#c19a82)" role="img" aria-label="Photo of a smile with a tooth shade guide held beside it"></div>
    <div class="brand-name" style="left:50px;top:322px">q7r Dental</div>
    <ul class="contact" style="left:50px;top:380px">
      <li><svg width="10" height="10" viewBox="0 0 24 24"><path fill="var(--navy)" d="M6.6 10.8a15 15 0 0 0 6.6 6.6l2.2-2.2c.3-.3.7-.4 1-.2 1.1.4 2.3.6 3.6.6.6 0 1 .4 1 1V20c0 .6-.4 1-1 1A17 17 0 0 1 3 4c0-.6.4-1 1-1h3.5c.6 0 1 .4 1 1 0 1.3.2 2.5.6 3.6.1.3 0 .7-.2 1z"/></svg>240-555-0187</li>
      <li><svg width="10" height="10" viewBox="0 0 24 24"><circle cx="12" cy="12" r="9" fill="none" stroke="var(--navy)" stroke-width="2"/><path d="M3 12h18M12 3c3 3 3 15 0 18M12 3c-3 3-3 15 0 18" fill="none" stroke="var(--navy)" stroke-width="1.6"/></svg>www.q7rdental.com</li>
      <li><svg width="10" height="12" viewBox="0 0 24 28"><path fill="var(--navy)" d="M12 0a9 9 0 0 0-9 9c0 7 9 19 9 19s9-12 9-19a9 9 0 0 0-9-9zm0 12a3 3 0 1 1 0-6 3 3 0 0 1 0 6z"/></svg>1180 Maple Crest Rd,<br>Greenfield, MD 20910</li>
    </ul>
  </div>
  <div class="fold" style="left:555.33px"></div>

  <div class="panel panel--3">
    <div class="brand-name" style="left:40px;top:28px">q7r Dental</div>
    <div class="photo photo--circle" style="left:38px;top:80px;width:200px;height:200px;background:radial-gradient(circle at 50% 40%,#fbf3e6,#e9d2b4 60%,#d7b48d)" role="img" aria-label="Photo of a smiling senior couple sharing red apples"></div>
    <div class="tagline" style="top:350px">
      <div class="tagline__lead">Going to the Dentist</div>
      <div class="tagline__big">CAN BE FUN</div>
      <div class="tagline__tail">We Put Smile in your Life</div>
    </div>
  </div>
</section>

<section class="sheet sheet--inside" aria-label="Brochure inside">
  <svg class="photo" style="left:0;top:0" width="833" height="560" aria-hidden="true">
    <path d="M555.33 250 Q700 200 833 230 L833 560 L555.33 560 Z" fill="var(--teal-pale)"/>
    <path d="M555.33 500 Q700 470 833 470 L833 560 L555.33 560 Z" fill="var(--teal-soft)"/>
    <path d="M0 468 L555.33 468" stroke="var(--lime)" stroke-width="4"/>
    <path d="M0 474 L555.33 474" stroke="var(--teal)" stroke-width="3"/>
  </svg>
  <div class="photo" style="left:277.67px;top:0;width:555.33px;height:170px;background:linear-gradient(90deg,#f4f6f8,#e4e8ec 55%,#f3c8c0);border-bottom-left-radius:60% 40px" role="img" aria-label="Illustration of a row of teeth with a dental implant screw"></div>
  <div class="photo" style="left:0;top:478px;width:555.33px;height:82px;background:linear-gradient(90deg,#0e2f6b,#3f7cc4 50%,#123a7a)" role="img" aria-label="Blue dental x-ray image of a jaw"></div>

  <div class="panel panel--1">
    <div class="tab" style="left:0;top:24px">Implant Restoration</div>
    <div class="body-text" style="left:18px;top:48px;width:245px">
      <p>Dental implants are another form of cosmetic solution in cases where Crowns and Bridges are less attractive solutions. Therefore, it requires proper examination to qualify a patient for Dental Implants, following which a decision is made based mostly on the assessed outcome of such a procedure. The dental implant candidate must have sufficient bone and adequately healthy gums to allow the implant treatment to be successful.</p>
      <p>Dental implants are long term treatment for replacing missing tooth and are considered superior to Dentures. q7r Dental issues a warning that certain conditions including, but not limited to, Gum Loss, Bone Loss, Smoking like make implants more susceptible to failures; however, reports of success are not that uncommon.</p>
    </div>
    <div class="tab" style="left:0;top:232px">Bonded Fillings</div>
    <div class="body-text" style="left:18px;top:256px;width:245px">
      <p>Bonding is another term for a composite or tooth colored restoration which is used to treat a decayed, fractured or chipped teeth. It can sometimes be used to treat discolored teeth or to make a composite veneer. This procedure is known as bonding because of how the filling bonds to adheres to the tooth structure.</p>
      <p>Bonded fillings are used for cosmetic purposes to restore or enhance the tooth structure of a chipped, decayed or an otherwise discolored tooth in a single visit. A tooth colored resin material is applied using adhesive and are then set under the application of high intensity curing light.</p>
      <p>For tooth decay, bond filling are good alternative to Amalgam filling. In dental terms, there are two broad uses, firstly as a bonding agent in a Direct Composite Bonding for a minimally invasive smile makeovers, and secondly as a bonding agent in the process of attaching restoration to the tooth for e.g. crowns and bridges to the tooth.</p>
    </div>
  </div>
  <div class="fold" style="left:277.67px"></div>

  <div class="panel panel--2">
    <div class="photo photo--circle" style="left:45px;top:100px;width:150px;height:150px;background:radial-gradient(circle at 50% 40%,#d9b79c,#8c7a5e 60%,#4f6b3e)" role="img" aria-label="Photo of a senior man eating a red apple"></div>
    <div class="tab" style="left:0;top:272px">Restauración de Implantes</div>
    <div class="body-text" style="left:18px;top:296px;width:245px">
      <p>Los implantes dentales son otra forma de solución cosmética en los casos en que las coronas y los puentes son soluciones menos atractivas. Por lo tanto, requiere un examen adecuado para calificar a un paciente para implantes dentales, tras lo cual se toma una decisión basada principalmente en el resultado evaluado de dicho procedimiento. El candidato para implante dental debe tener suficiente hueso y encías saludables para permitir que el tratamiento con implantes tenga éxito.</p>
      <p>Los implantes dentales son un tratamiento a largo plazo para reemplazar los dientes perdidos y se consideran superiores a las dentaduras postizas. q7r Dental emite una advertencia de que ciertas afecciones que incluyen, entre otras, la pérdida de las encías, la pérdida ósea, el tabaquismo, hacen que los implantes sean más susceptibles a fallas; sin embargo, los informes de éxito no son tan infrecuentes.</p>
    </div>
  </div>
  <div class="fold" style="left:555.33px"></div>

  <div class="panel panel--3">
    <div class="photo photo--circle" style="left:70px;top:100px;width:140px;height:140px;background:radial-gradient(circle at 50% 45%,#e8c9b3,#6b4f45 65%,#d8c14a)" role="img" aria-label="Photo of a smiling young woman"></div>
    <div class="tab" style="left:0;top:268px">Rellenos en condiciones de servidumbre</div>
    <div class="body-text" style="left:18px;top:292px;width:245px">
      <p>La vinculación es otro término para una restauración compuesta o coloreada del diente que se utiliza para tratar dientes descompuestos, fracturados o astillados. A veces se puede usar para tratar dientes descoloridos o para hacer una chapa compuesta. Este procedimiento se conoce como unión debido a cómo se adhiere el relleno a la estructura del diente.</p>
      <p>Los empastes en condiciones de servidumbre se utilizan con fines cosméticos para restaurar o mejorar la estructura dental de un diente astillado, cariado o decolorado en una sola visita. Un material de resina del color del diente se aplica con adhesivo y luego se configura bajo la aplicación de luz de curado de alta intensidad.</p>
      <p>Para la caries dental, el relleno de enlace es una buena alternativa al llenado de amalgama. En términos dentales, existen dos amplios usos, en primer lugar como un agente de unión en una unión compuesta directa para cambios de sonrisa mínimamente invasivos, y en segundo lugar como un agente de unión en el proceso de fijación de la restauración del diente, por ejemplo, coronas y puentes al diente.</p>
    </div>
  </div>
</section>

</body>
</html>
```